New Infographic Design Project

I need a 1 page Infographic that explains our Quillstone Prism offer.

Can you use the following content in the attached document to create a 1 page infographic. The image in the bottom of the document is one of our competitors who is offering the same thing, this image is only provided for inspiration and ideas as we need ours to be based on the content of the document and aligned with the Corvenly Brand

```html
<!DOCTYPE html>
<html lang="en">
<head>
<meta charset="utf-8">
<title>Data Ready. AI Ready. In 6 Weeks. — Corvenly</title>
<link rel="stylesheet" href="https://fonts.googleapis.com/css2?family=Montserrat:wght@700;800;900&family=Poppins:wght@400;500;600&display=swap">
<style>
  :root {
    --navy: #0c1f40;
    --navy-deep: #091833;
    --path: #35507d;
    --line: #4f6c9c;
    --orange: #ff8a00;
    --steel: #8fa7cd;
    --white: #ffffff;
    --muted: #a7b5cc;
    --icon-tile: #3f5f8f;
    --card-1: #172f59;
    --card-2: #213c69;
    --card-3: #2c4978;
    --card-4: #3a5888;
  }
  * { box-sizing: border-box; margin: 0; padding: 0; }
  html, body { width: 1200px; height: 852px; overflow: hidden; }
  body {
    background: radial-gradient(ellipse at 55% 50%, #10264d 0%, var(--navy) 55%, var(--navy-deep) 100%);
    font-family: "Poppins", sans-serif;
    color: var(--white);
    position: relative;
  }
  .display { font-family: "Montserrat", sans-serif; font-weight: 900; }
  .abs { position: absolute; }

  /* Headline */
  .headline-frame { left: 44px; top: 37px; width: 596px; height: 60px;
    border: 2px solid var(--line); border-right: none; border-radius: 32px 0 0 32px; }
  .headline-lead { left: 74px; top: 46px; font-size: 35px; letter-spacing: 3px; line-height: 40px; white-space: nowrap; }
  .headline-lead .ai { color: var(--steel); margin-left: 14px; }
  .headline-weeks { left: 646px; top: 26px; font-size: 80px; line-height: 80px; color: var(--orange); letter-spacing: 2px; white-space: nowrap; }

  /* Partner box */
  .partner { left: 44px; top: 129px; width: 364px; height: 262px;
    border: 2px solid var(--line); border-radius: 26px; }
  .partner-title { left: 42px; top: 156px; background: var(--navy); font-size: 20.5px; line-height: 21px; padding: 0 4px 6px 2px; font-weight: 800; }
  .partner-body { left: 69px; top: 224px; width: 330px; font-size: 12px; line-height: 14.8px; }
  .partner-body p + p { margin-top: 12px; color: var(--steel); font-weight: 600; }

  /* Edge list */
  .edge-title { left: 44px; top: 437px; font-size: 21px; font-weight: 800; color: var(--steel); }
  .edge-item { left: 43px; width: 420px; height: 68px; }
  .edge-icon { position: absolute; left: 0; top: 0; width: 63px; height: 63px; background: var(--icon-tile); border-radius: 8px; }
  .edge-icon svg { width: 63px; height: 63px; }
  .edge-name { position: absolute; left: 76px; top: 2px; font-size: 15.5px; font-weight: 600; white-space: nowrap; }
  .edge-desc { position: absolute; left: 76px; top: 28px; width: 300px; font-size: 11.5px; line-height: 14.5px; color: var(--muted); }

  /* Timeline */
  .timeline-title { left: 461px; top: 133px; font-size: 21px; line-height: 21px; font-weight: 800; }
  .step-name { font-size: 14.5px; font-weight: 600; line-height: 15.5px; }
  .step-desc { font-size: 11.5px; line-height: 14px; color: var(--muted); margin-top: 5px; }
  .step.right { text-align: right; right: 306px; width: 200px; }
  .step.left { left: 461px; width: 215px; }

  /* Extra edge */
  .extra-title { left: 978px; top: 126px; font-size: 21px; font-weight: 800; }
  .extra-card { left: 957px; width: 201px; border: 2px solid var(--line); border-radius: 24px; }
  .extra-card .icon { position: absolute; left: 14px; top: 18px; width: 36px; height: 36px; }
  .extra-card h3 { position: absolute; left: 56px; top: 16px; font-size: 14.5px; line-height: 15px; font-weight: 600; }
  .extra-card p { position: absolute; left: 16px; top: 66px; width: 170px; font-size: 11.5px; line-height: 14px; color: #c6d1e2; }
</style>
</head>
<body>

<header>
  <div class="abs headline-frame"></div>
  <h1>
    <span class="abs display headline-lead">DATA READY.<span class="ai">AI READY.</span></span>
    <span class="abs display headline-weeks">IN 6 WEEKS.</span>
  </h1>
</header>

<section>
  <div class="abs partner"></div>
  <h2 class="abs display partner-title">YOUR LONG-TERM<br>STRATEGIC DATA PARTNER</h2>
  <div class="abs partner-body">
    <p>We start with a Business Data Assessment or Prism Deployment Assessment to pinpoint the highest-value use cases, the biggest data risks, and the fastest path to impact.</p>
    <p>We stand up a governed Quillstone Prism foundation using repeatable ingestion, validation, and common data model patterns, so your reporting scales cleanly and your AI initiatives provide business value.</p>
  </div>
</section>

<section>
  <h2 class="abs display edge-title">THE CORVENLY EDGE</h2>

  <div class="abs edge-item" style="top:477px">
    <div class="edge-icon"><svg viewBox="0 0 63 63"><circle cx="31.5" cy="27" r="14" fill="none" stroke="#1b2f55" stroke-width="2.5"/><path d="M24 38l-4 11 6-2 3 5 2-12M39 38l4 11-6-2-3 5-2-12" fill="none" stroke="#1b2f55" stroke-width="2.5"/><path d="M31.5 19l2.4 5 5.4.6-4 3.7 1.1 5.3-4.9-2.7-4.9 2.7 1.1-5.3-4-3.7 5.4-.6z" fill="var(--orange)"/></svg></div>
    <h3 class="edge-name">Quality-first delivery</h3>
    <p class="edge-desc">Automated validation, data tests, and “quality gates” that stop bad data upstream.</p>
  </div>

  <div class="abs edge-item" style="top:566px">
    <div class="edge-icon"><svg viewBox="0 0 63 63"><rect x="14" y="20" width="28" height="26" rx="2" fill="none" stroke="#1b2f55" stroke-width="2.5"/><path d="M22 20v-5a6 6 0 0 1 12 0v5M19 28v10" fill="none" stroke="#1b2f55" stroke-width="2.5"/><rect x="34" y="33" width="15" height="14" rx="2" fill="none" stroke="var(--orange)" stroke-width="3"/></svg></div>
    <h3 class="edge-name">Data products, not datasets</h3>
    <p class="edge-desc">Clear ownership, SLAs, versioning, and reusable, consumable outputs aligned to high impact business outcomes.</p>
  </div>

  <div class="abs edge-item" style="top:655px">
    <div class="edge-icon"><svg viewBox="0 0 63 63"><path d="M31.5 12v8" stroke="#1b2f55" stroke-width="2"/><path d="M32 11h8l-2 3 2 3h-8z" fill="var(--orange)"/><path d="M20 30a11.5 10 0 0 1 23 0zM18 32h27M21 36v10M27 36v10M33 36v10M39 36v10M15 48h33" fill="none" stroke="#1b2f55" stroke-width="2.5"/></svg></div>
    <h3 class="edge-name">Governance that doesn’t slow you down</h3>
    <p class="edge-desc">Security, access, lineage, and auditability built in from day one.</p>
  </div>

  <div class="abs edge-item" style="top:743px">
    <div class="edge-icon"><svg viewBox="0 0 63 63"><circle cx="31.5" cy="31.5" r="14" fill="none" stroke="#1b2f55" stroke-width="2" stroke-dasharray="3 3"/><path d="M31.5 6v8M31.5 49v8M6 31.5h8M49 31.5h8M14 14l5 5M49 14l-5 5M14 49l5-5M49 49l-5-5" stroke="#1b2f55" stroke-width="2.5"/><path d="M26 28l5.5-3 5.5 3v6l-5.5 3-5.5-3z" fill="none" stroke="var(--orange)" stroke-width="2.5"/></svg></div>
    <h3 class="edge-name">Operate seamlessly</h3>
    <p class="edge-desc">CI/CD, monitoring, and cost controls so the platform stays healthy.</p>
  </div>
</section>

<section>
  <h2 class="abs display timeline-title">6 WEEK<br>TIME<br>TO<br>VALUE</h2>

  <svg class="abs" style="left:0;top:0" width="1200" height="852" aria-hidden="true">
    <path d="M596 168 V187 A56 56 0 0 0 652 243 H734 A56 56 0 0 1 734 355 H652 A56 56 0 0 0 652 466 H734 A56 56 0 0 1 734 578 H652 A56 56 0 0 0 652 690 H734 A56 56 0 0 1 790 746 V743" fill="none" stroke="var(--path)" stroke-width="8"/>
    <path d="M596 168 V128 M790 743 V808" stroke="var(--path)" stroke-width="8" stroke-linecap="round"/>
    <defs><linearGradient id="bubble" x1="0" y1="0" x2="1" y2="1"><stop offset="0" stop-color="#b8c9e4"/><stop offset="1" stop-color="#5f7fb0"/></linearGradient></defs>
    <g fill="url(#bubble)">
      <circle cx="648" cy="211" r="32"/><circle cx="735" cy="311" r="32"/><circle cx="652" cy="408" r="32"/>
      <circle cx="733" cy="503" r="32"/><circle cx="652" cy="597" r="32"/><circle cx="735" cy="700" r="32"/>
    </g>
    <g fill="none" stroke="#1b2f55" stroke-width="2.2">
      <path d="M648 197a9 9 0 0 1 5 16v4h-10v-4a9 9 0 0 1 5-16z" fill="var(--orange)"/><path d="M644 221h8M645 225h6"/>
      <path d="M735 296a8 8 0 0 1 8 8c0 6-8 13-8 13s-8-7-8-13a8 8 0 0 1 8-8z" stroke="var(--orange)"/><path d="M725 326l4-9h12l4 9z"/>
      <rect x="641" y="394" width="17" height="26" rx="2"/><path d="M644 401h10M644 406h10M644 411h8" stroke="var(--orange)"/><path d="M663 396v18l2 4 2-4v-18z"/>
      <rect x="721" y="488" width="24" height="8"/><rect x="721" y="499" width="24" height="8"/><rect x="721" y="510" width="24" height="8"/><path d="M716 521h34"/>
      <path d="M638 589h28M638 597h28M638 605h28"/><circle cx="645" cy="589" r="3" fill="var(--orange)"/><circle cx="657" cy="597" r="3" fill="var(--orange)"/><circle cx="645" cy="605" r="3" fill="var(--orange)"/>
      <rect x="723" y="688" width="24" height="24" rx="2"/><path d="M728 684v4M735 684v4M742 684v4M728 712v4M735 712v4M742 712v4M719 693h4M719 700h4M719 707h4M747 693h4M747 700h4M747 707h4"/><circle cx="735" cy="700" r="6" fill="var(--orange)" stroke="none"/>
    </g>
  </svg>

  <div class="abs step right" style="top:172px"><h3 class="step-name">Envision &amp; Assess</h3><p class="step-desc">Use case shortlist &amp; priority based on highest business impact, current-state review, data risk &amp; compliance priorities, target operating model.</p></div>
  <div class="abs step left" style="top:282px"><h3 class="step-name">Architecture &amp;<br>governance design</h3><p class="step-desc">Landing zone decisions, security &amp; access model, patterns/standards, delivery plan &amp; success metrics.</p></div>
  <div class="abs step right" style="top:375px"><h3 class="step-name">Prism foundation<br>deployed</h3><p class="step-desc">Workspaces and environments, automation &amp; CI/CD, onboarding playbooks, baseline policies/ guardrails.</p></div>
  <div class="abs step left" style="top:475px"><h3 class="step-name">Data ingestion +<br>validation framework</h3><p class="step-desc">Reusable ingestion patterns, automated validation, data contracts/SLAs, observability signals &amp; alerting.</p></div>
  <div class="abs step right" style="top:573px"><h3 class="step-name">Scalable common<br>data model</h3><p class="step-desc">Domain model, master entities, curated layer, semantic modelling patterns that support Lumeboard at scale.</p></div>
  <div class="abs step left" style="top:673px;width:225px"><h3 class="step-name">Business outcomes<br>+ AI-ready capability</h3><p class="step-desc">Executive dashboards &amp; priority reports, performance optimisation, hypercare &amp; handover, AI readiness check and pilot plan (predictive analytics &amp;/or secure enterprise LLM).</p></div>
</section>

<section>
  <h2 class="abs display extra-title">EXTRA EDGE</h2>

  <article class="abs extra-card" style="top:164px;height:165px;background:var(--card-1);z-index:4">
    <svg class="icon" viewBox="0 0 36 36" fill="none" stroke="#9fb4d6" stroke-width="2"><rect x="12" y="4" width="14" height="14" rx="2"/><circle cx="19" cy="11" r="3.5" fill="var(--orange)" stroke="none"/><path d="M3 30l6-5h10l7-4M3 33h12l14-7"/></svg>
    <h3>“AI-ready data” guarantee</h3>
    <p>Every priority dataset ships with validation rules, ownership, lineage, and freshness SLAs before it can power AI.</p>
  </article>

  <article class="abs extra-card" style="top:298px;height:193px;background:var(--card-2);z-index:3">
    <svg class="icon" style="top:46px" viewBox="0 0 36 36" fill="none" stroke="#9fb4d6" stroke-width="2"><circle cx="9" cy="6" r="3.5"/><path d="M4 22v-8h10v8M7 22v10M11 22v10M20 5h10M20 10h10"/><path d="M27 18a7 7 0 1 0 7 7h-7z" fill="var(--orange)" stroke="none"/></svg>
    <h3 style="top:46px">Cost-to-serve transparency</h3>
    <p style="top:98px">Show business owners what each product/report costs to run and optimise it continuously.</p>
  </article>

  <article class="abs extra-card" style="top:460px;height:192px;background:var(--card-3);z-index:2">
    <svg class="icon" style="top:44px" viewBox="0 0 36 36" fill="none" stroke="#9fb4d6" stroke-width="2"><circle cx="18" cy="18" r="12" stroke-dasharray="2 4"/><circle cx="18" cy="18" r="6" stroke="var(--orange)"/><rect x="15.5" y="17" width="5" height="4" fill="var(--orange)" stroke="none"/></svg>
    <h3 style="top:44px">Change-proof pipelines</h3>
    <p style="top:100px">Data contracts + automated tests reduce breakages from upstream schema changes.</p>
  </article>

  <article class="abs extra-card" style="top:621px;height:187px;background:var(--card-4);z-index:1">
    <svg class="icon" style="top:44px" viewBox="0 0 36 36" fill="none" stroke="#b4c4de" stroke-width="2"><circle cx="6" cy="6" r="3"/><path d="M3 20v-8h8l6-3M5 20v-2"/><rect x="15" y="4" width="18" height="12" stroke="var(--orange)"/><circle cx="6" cy="27" r="2.5"/><circle cx="18" cy="27" r="2.5"/><circle cx="30" cy="27" r="2.5"/><path d="M2 34a4 4 0 0 1 8 0M14 34a4 4 0 0 1 8 0M26 34a4 4 0 0 1 8 0"/></svg>
    <h3 style="top:44px">Governed<br>self-serve</h3>
    <p style="top:100px">Catalog + certified datasets so teams move faster without creating data chaos.</p>
  </article>
</section>

</body>
</html>
```